Gin bottle designs - micro distillery

We are an Italian Distillery in Melbourne Australia. We would like to modernise the brand and in particular the bottle labels. We need to get a lable that will look better on the shelf while still maintaining the Italian "feel" of the product.

You can also refer to web site: www.verantocellars.com for a background.

At this time we are stuck with the rectangular bottles. We can consider different configurations (like a top label and a wrap around label at the bottom

The key message is more modern and attention grabbing.

Target Market(s)

Alcohol drinkers

Requirements
Must have
• GIN
Mediterranean Gin
Grappa
Brandy
Vodka

```html
<!DOCTYPE html>
<html lang="en">
<head>
<meta charset="utf-8">
<title>Veranto Gin Labels</title>
<link rel="stylesheet" href="https://fonts.googleapis.com/css2?family=Playfair+Display:wght@600;700&family=Courier+Prime:wght@400;700&family=Dancing+Script:wght@500&family=Oswald:wght@400;500&display=swap">
<style>
  :root {
    --backdrop: #f3f1ea;
    --label: #fdfdfb;
    --label-edge: #d9d6cc;
    --brand-green: #2f6b35;
    --ink: #1f1f1f;
    --gold: #c9a83a;
    --grappa-red: #c8262b;
    --band: #2b2b2b;
    --band-text: #f1ead2;
    --italy-green: #2e8b43;
    --italy-red: #cf2b30;
    --scene-light: #e6e6e3;
    --scene-dark: #6f6f6b;
  }
  * { box-sizing: border-box; margin: 0; padding: 0; }
  html, body { width: 1200px; height: 2480px; overflow: hidden; }
  body { background: var(--backdrop); position: relative; }

  .label {
    position: absolute;
    top: 200px;
    width: 460px;
    height: 2080px;
    background: var(--label);
    border: 2px solid var(--label-edge);
    display: flex;
    flex-direction: column;
    align-items: center;
  }
  .label--mediterranean { left: 70px; }
  .label--grappa { left: 670px; }

  .brand {
    margin-top: 70px;
    display: flex;
    align-items: center;
    gap: 18px;
    height: 240px;
  }
  .brand__dot {
    width: 30px; height: 30px;
    border-radius: 50%;
    background: var(--brand-green);
  }
  .brand__name {
    font-family: "Playfair Display", serif;
    font-weight: 700;
    font-size: 60px;
    letter-spacing: 4px;
    color: var(--brand-green);
  }

  .vineyard {
    margin-top: 40px;
    width: 400px;
    height: 1080px;
    border-radius: 200px 200px 0 0;
    background: linear-gradient(180deg, var(--scene-light) 0%, #bdbdb8 35%, var(--scene-dark) 70%, #8c8c87 100%);
  }

  .product {
    margin-top: 60px;
    text-align: center;
  }
  .product__variant {
    font-family: "Courier Prime", monospace;
    font-weight: 700;
    font-size: 34px;
    letter-spacing: 6px;
    color: var(--gold);
  }
  .product__variant--grappa {
    font-family: "Oswald", sans-serif;
    font-weight: 500;
    font-size: 52px;
    color: var(--grappa-red);
  }
  .product__name {
    font-family: "Oswald", sans-serif;
    font-weight: 500;
    font-size: 120px;
    line-height: 1;
    color: var(--ink);
    letter-spacing: 4px;
  }

  .heritage {
    margin-top: 24px;
    width: 380px;
    background: var(--band);
    border: 3px double var(--gold);
    padding: 10px 0 8px;
    text-align: center;
    font-family: "Playfair Display", serif;
    color: var(--band-text);
  }
  .heritage__main { font-size: 34px; letter-spacing: 2px; }
  .heritage__sub { font-family: "Courier Prime", monospace; font-size: 20px; letter-spacing: 4px; }

  .signoff {
    margin-top: 18px;
    width: 380px;
    display: flex;
    justify-content: space-between;
    align-items: center;
  }
  .tricolour { display: flex; gap: 6px; }
  .tricolour span { width: 22px; height: 22px; border-radius: 50%; border: 1px solid #bbb; }
  .tricolour .g { background: var(--italy-green); }
  .tricolour .w { background: #fff; }
  .tricolour .r { background: var(--italy-red); }
  .signoff__name {
    font-family: "Dancing Script", cursive;
    font-size: 34px;
    color: var(--grappa-red);
  }

  .facts {
    margin-top: auto;
    margin-bottom: 40px;
    width: 380px;
    display: flex;
    justify-content: space-between;
    font-family: "Oswald", sans-serif;
    font-size: 28px;
    color: var(--ink);
  }
</style>
</head>
<body>

  <section class="label label--mediterranean">
    <div class="brand"><span class="brand__dot"></span><span class="brand__name">VERANTO</span></div>
    <div class="vineyard" role="img" aria-label="Engraved illustration of vineyard rows under a cloudy sky"></div>
    <div class="product">
      <div class="product__variant">MEDITERRANEAN</div>
      <div class="product__name">GIN</div>
    </div>
    <div class="heritage">
      <div class="heritage__main">ITALIAN HERITAGE</div>
      <div class="heritage__sub">AUSSIE SPIRIT</div>
    </div>
    <div class="signoff">
      <div class="tricolour"><span class="g"></span><span class="w"></span><span class="r"></span></div>
      <div class="signoff__name">Lia Moretti</div>
    </div>
    <div class="facts"><span>300mL</span><span>25% ALC/VOL</span></div>
  </section>

  <section class="label label--grappa">
    <div class="brand"><span class="brand__dot"></span><span class="brand__name">VERANTO</span></div>
    <div class="vineyard" role="img" aria-label="Engraved illustration of vineyard rows under a cloudy sky"></div>
    <div class="product">
      <div class="product__variant product__variant--grappa">GRAPPA</div>
      <div class="product__name">GIN</div>
    </div>
    <div class="heritage">
      <div class="heritage__main">ITALIAN HERITAGE</div>
      <div class="heritage__sub">AUSSIE SPIRIT</div>
    </div>
    <div class="signoff">
      <div class="tricolour"><span class="g"></span><span class="w"></span><span class="r"></span></div>
      <div class="signoff__name">Lia Moretti</div>
    </div>
    <div class="facts"><span>300mL</span><span>25% ALC/VOL</span></div>
  </section>

</body>
</html>
```